Torvane Template Design for Pressmoor Quillpath Site

We need graphic design and theme design work for our new site that will be running Quillpath with Torvane as the theme.

We have a draft logo that needs a graphic designer to improve it.

We are looking for sleek, modern, design that while minimal is distinct. ie page elements, content enhancement, block design that can be used, reused by in-house team.
This means there will also need to be a guide created on how to create, insert, edit each of those elements so that they can be used on new pages over time.

We have several businesses for which this is the "umbrella company" and so we will want to unify the colours and have identified a palette from which to start.

Some examples of site design we would like to stand up like:
https://www.zlt-example.com/
https://latchpromo-example.com/
https://business.veltrix-example.com/
https://www.norvask-example.com/learning/home.aspx

When I say "coded" below, this really just means the CSS needed for page elements.

Target Market(s)

Small firms in professional services - engineers, land surveyors, consultants

Number of Pages Required

3 page

Font styles to use
Sans Serif

Requirements
Must have
• Pressmoor/Torvane as base template, full home page layout with lorem ipsum placeholder
Nice to have
• custom blocks for pull quotes, call to action, a better design on the logo so it doesn't look like a rainbow.
Should not have
• Need for Blockwright

```html
<!DOCTYPE html>
<html lang="en">
<head>
<meta charset="utf-8">
<title>Kelvora – Home</title>
<link href="https://fonts.googleapis.com/css2?family=Lato:ital,wght@0,300;0,400;0,700;1,400&family=Montserrat:wght@500;600;700&display=swap" rel="stylesheet">
<style>
:root{
  --backdrop:#b3b3b3;
  --page:#ffffff;
  --soft:#f5f5f5;
  --ink:#111111;
  --muted:#444444;
  --white:#ffffff;
  --gold:#e0a01c;
  --green:#5cc36a;
  --teal:#13a3b8;
  --blue:#1d6fc2;
  --violet:#5a2f8f;
  --navy:#2f3a66;
}
*{box-sizing:border-box;margin:0;padding:0}
html,body{width:1200px;height:2500px;overflow:hidden}
body{background:var(--backdrop);font-family:"Lato",sans-serif;color:var(--ink);position:relative}
.page{position:absolute;left:81px;top:81px;width:1038px;height:2339px;background:var(--page);overflow:hidden;box-shadow:0 2px 10px rgba(0,0,0,.2)}
.abs{position:absolute}

/* hero */
.hero{position:absolute;left:0;top:0;width:1038px;height:590px;
  background:
    radial-gradient(ellipse 520px 420px at 0% 55%, rgba(224,160,28,.95), rgba(224,160,28,0) 70%),
    radial-gradient(ellipse 420px 300px at 25% 10%, rgba(110,190,90,.9), rgba(110,190,90,0) 70%),
    linear-gradient(100deg,#c8a02a 0%,#7fb24a 22%,#1e9fa6 42%,#1f6db8 60%,#4b3a97 78%,#5a2a8a 100%);}
.hero-wave{position:absolute;left:0;top:500px;width:1038px;height:90px}
.brand-badge{position:absolute;left:-20px;top:-40px;width:155px;height:120px;background:var(--white);border-radius:0 0 80px 60px;box-shadow:0 6px 0 rgba(240,200,40,.7)}
.brand-name{position:absolute;left:12px;top:10px;font:400 34px "Lato",sans-serif;color:var(--ink);letter-spacing:-.5px}
.nav{position:absolute;top:13px;left:0;width:1038px;font:600 10px "Montserrat",sans-serif;color:var(--white)}
.nav a{position:absolute;color:var(--white);text-decoration:none;top:2px}
.nav .current{font-weight:700}
.nav .contact-btn{top:-4px;left:966px;width:61px;height:21px;border:1px solid var(--white);border-radius:11px;text-align:center;line-height:19px;font-weight:500}
.hero-title{position:absolute;top:210px;width:1038px;text-align:center;font:300 40px "Lato",sans-serif;color:var(--white)}
.hero-title b{font-weight:700}
.hero-text{position:absolute;top:265px;left:269px;width:500px;text-align:center;font:300 15px/27px "Lato",sans-serif;color:var(--white)}
.btn-outline{position:absolute;border:1.5px solid var(--white);color:var(--white);text-align:center;font-family:"Montserrat",sans-serif;font-weight:600}
.hero-btn{left:451px;top:370px;width:137px;height:30px;border-radius:15px;line-height:27px;font-size:11px}

/* why */
.why{position:absolute;left:0;top:585px;width:1038px;height:467px;background:var(--soft)}
.section-title{position:absolute;width:1038px;text-align:center;font:300 36px "Lato",sans-serif}
.section-title b{font-weight:700}
.section-sub{position:absolute;width:1038px;text-align:center;font:400 12px "Lato",sans-serif}
.card{position:absolute;background:var(--white);border-radius:10px;text-align:center}
.card.featured{border:1.5px solid transparent;background:linear-gradient(var(--white),var(--white)) padding-box,linear-gradient(135deg,var(--gold),var(--green),var(--teal),var(--blue),var(--violet)) border-box}
.why .card{top:167px;width:270px;height:207px}
.card-icon{position:absolute;left:105px;top:24px;width:60px;height:58px}
.card-title{position:absolute;left:0;width:100%;font:400 15px "Lato",sans-serif}
.card-body{position:absolute;left:28px;right:28px;font:400 8.6px/14px "Lato",sans-serif;color:var(--muted)}
.why .card-title{top:96px}
.why .card-body{top:124px}

/* courses */
.courses{position:absolute;left:0;top:1052px;width:1038px;height:569px;background:var(--white)}
.courses .card{top:166px;width:270px;height:311px;background:var(--soft)}
.courses .card.featured{background:linear-gradient(var(--soft),var(--soft)) padding-box,linear-gradient(135deg,var(--gold),var(--green),var(--teal),var(--blue),var(--violet)) border-box}
.course-photo{position:absolute;left:0;top:0;width:100%;height:155px;border-radius:10px 10px 12px 12px}
.photo-survey{background:linear-gradient(160deg,#6f6a5c,#9c6b3e 45%,#4a3c30)}
.photo-team{background:linear-gradient(150deg,#e9ecef,#c9ced4 50%,#f0a050 80%,#3a3a3a)}
.photo-estimate{background:linear-gradient(150deg,#d7dde3,#b9c2cc 55%,#e3a53a 85%)}
.courses .card-title{top:177px;font-size:13.5px}
.courses .card-body{top:205px;left:26px;right:26px}
.course-tags{position:absolute;top:275px;width:100%;font:italic 400 8.5px "Lato",sans-serif;color:var(--muted)}

/* testimonial */
.quote-band{position:absolute;left:0;top:1621px;width:1038px;height:260px;background:var(--soft)}
.pull-quote{position:absolute;left:200px;top:84px;width:640px;padding-left:10px;border-left:2px solid;border-image:linear-gradient(var(--violet),var(--blue),var(--green),var(--gold)) 1}
.pull-quote p{font:300 15.5px/23px "Lato",sans-serif;color:var(--muted)}
.pull-quote cite{display:block;font:400 9px "Lato",sans-serif;font-style:normal;color:var(--muted);margin-top:2px}

/* cta */
.cta{position:absolute;left:0;top:1830px;width:1038px;height:336px;
  background:
    radial-gradient(ellipse 380px 260px at 0% 100%, rgba(250,170,20,1), rgba(250,190,20,0) 70%),
    linear-gradient(100deg,#c59a2c 0%,#7dc252 22%,#1fb7b0 42%,#128fc9 55%,#4b4ba3 75%,#2f3a66 100%)}
.cta-wave{position:absolute;left:0;top:0;width:1038px;height:60px}
.cta-title{position:absolute;top:134px;width:1038px;text-align:center;font:300 36px "Lato",sans-serif;color:var(--white)}
.cta-title b{font-weight:700}
.cta-text{position:absolute;top:178px;width:1038px;text-align:center;font:400 15px/24px "Lato",sans-serif;color:var(--white)}
.cta-btn{left:436px;top:240px;width:157px;height:34px;border-radius:17px;line-height:31px;font-size:16px;letter-spacing:1.5px}

/* footer */
.footer{position:absolute;left:0;top:2166px;width:1038px;height:173px;background:var(--white)}
.footer-brand{position:absolute;left:174px;top:46px;font:400 44px "Lato",sans-serif;letter-spacing:-.5px}
.footer-about{position:absolute;left:350px;top:56px;width:210px;font:400 7.8px/14px "Lato",sans-serif;color:var(--muted)}
.footer-col{position:absolute;top:52px}
.footer-col h4{font:400 13px "Lato",sans-serif;margin-bottom:4px}
.footer-col li{list-style:none;font:400 8.5px/14px "Lato",sans-serif;color:var(--muted)}
.footer-nav li::before{content:"\25B8 ";color:var(--muted)}
.footer-contact li{display:flex;align-items:center;gap:4px;margin-bottom:4px}
.dot{width:11px;height:11px;border-radius:50%;background:linear-gradient(135deg,var(--gold),var(--teal),var(--violet));display:inline-flex;align-items:center;justify-content:center}
</style>
</head>
<body>
<div class="page">

  <header class="hero">
    <div class="brand-badge"></div>
    <div class="brand-name">Kelvora</div>
    <nav class="nav">
      <a class="current" style="left:713px">Home</a>
      <a style="left:772px">About</a>
      <a style="left:830px">Courses</a>
      <a style="left:898px">Services</a>
      <a class="contact-btn">Contact</a>
    </nav>
    <h1 class="hero-title"><b>Transform</b> Your Team’s Expertise</h1>
    <p class="hero-text">Kelvora delivers industry-tailored courses for engineering, surveying and consulting professionals. Build confidence, meet compliance requirements and stay ahead of the curve.</p>
    <a class="btn-outline hero-btn">Explore Courses</a>
    <svg class="hero-wave" viewBox="0 0 1038 90" preserveAspectRatio="none">
      <path d="M0 90 C120 88 260 84 380 86 C440 88 470 74 517 62 C580 46 620 40 700 40 C820 40 920 40 1038 38 L1038 90 Z" fill="#f5f5f5"/>
    </svg>
  </header>

  <section class="why">
    <h2 class="section-title" style="top:78px">Why Choose <b>Kelvora</b> ?</h2>
    <p class="section-sub" style="top:126px">Built for firms where expertise matters</p>

    <article class="card" style="left:87px">
      <svg class="card-icon" viewBox="0 0 60 58" fill="none" stroke="#111" stroke-width="1.6">
        <rect x="10" y="4" width="26" height="36" rx="2"/><rect x="5" y="9" width="26" height="40" rx="2"/>
        <path d="M10 18h16M10 24h16M10 30h10"/><path d="M30 38l16-7 12 7-14 6z"/><path d="M36 41v7c4 3 12 3 16 0v-7"/>
      </svg>
      <h3 class="card-title">Industry-Specific Courses</h3>
      <p class="card-body">Gain practical knowledge built around real-world challenges in architecture, engineering and land surveying. Our modules address standards, regulations and best practices unique to your field.</p>
    </article>

    <article class="card featured" style="left:385px">
      <svg class="card-icon" viewBox="0 0 60 58" fill="none" stroke="#111" stroke-width="1.6">
        <path d="M12 4h17v24H12zM31 4h17v24H31z"/><path d="M16 10h9M16 15h9M16 20h9M35 10h9M35 15h9M35 20h9"/>
        <circle cx="30" cy="44" r="9"/><path d="M30 39v5l3 3"/><path d="M16 38a8 8 0 0 0-2 12l-3 1M44 38a8 8 0 0 1 2 12l3 1"/>
      </svg>
      <h3 class="card-title">Flexible Learningt</h3>
      <p class="card-body">Learn at your own pace with on-demand lectures, downloadable resources and progress tracking. Whether you need a quick refresher or an in-depth course, Kelvora fits into busy schedules.</p>
    </article>

    <article class="card" style="left:683px">
      <svg class="card-icon" viewBox="0 0 60 58" fill="none" stroke="#111" stroke-width="1.6">
        <path d="M18 4l2 4 4 .5-3 3 1 4-4-2-4 2 1-4-3-3 4-.5zM30 2l2 4 4 .5-3 3 1 4-4-2-4 2 1-4-3-3 4-.5zM42 4l2 4 4 .5-3 3 1 4-4-2-4 2 1-4-3-3 4-.5z"/>
        <circle cx="30" cy="27" r="7"/><path d="M18 56V44c0-5 5-8 12-8s12 3 12 8v12"/><rect x="25" y="44" width="10" height="8"/>
      </svg>
      <h3 class="card-title">Expert Instructors</h3>
      <p class="card-body">Courses are developed and taught by professionals with decades of experience. You’ll benefit from insights, case studies and mentorship from leaders in your industry.</p>
    </article>
  </section>

  <section class="courses">
    <h2 class="section-title" style="top:78px">Explore Featured <b>Courses</b></h2>
    <p class="section-sub" style="top:126px">Courses designed to support technical excellence and professional growth.</p>

    <article class="card" style="left:87px">
      <div class="course-photo photo-survey" role="img" aria-label="Photo of a surveyor kneeling beside a tripod-mounted instrument on a construction site"></div>
      <h3 class="card-title">Fundamentals of Land Surveying</h3>
      <p class="card-body">Build a strong foundation in modern land surveying principles, tools, and workflows. This course covers core concepts, field practices, and industry standards essential for accurate and reliable survey work.</p>
      <p class="course-tags">Self-paced • On-demand • Practical focus</p>
    </article>

    <article class="card featured" style="left:385px">
      <div class="course-photo photo-team" role="img" aria-label="Overhead photo of an engineering team reviewing plans around a table with hard hats"></div>
      <h3 class="card-title">Project Management for Engineering Firms</h3>
      <p class="card-body">Learn practical project management strategies tailored specifically for engineering and consulting environments. Focus on scope control, scheduling, risk management, and delivering projects on time and on budget.</p>
      <p class="course-tags">Self-paced • On-demand • Practical focus</p>
    </article>

    <article class="card" style="left:683px">
      <div class="course-photo photo-estimate" role="img" aria-label="Photo of hands using a calculator over cost charts beside a yellow hard hat"></div>
      <h3 class="card-title">Construction Cost Estimating</h3>
      <p class="card-body">Develop the skills needed to prepare accurate and defensible construction cost estimates. This course explores quantity take-offs, pricing methods, budgeting, and real-world estimating scenarios.</p>
      <p class="course-tags">Self-paced • On-demand • Practical focus</p>
    </article>
  </section>

  <section class="quote-band">
    <blockquote class="pull-quote">
      <p>Kelvora’s training has empowered our firm to take on more complex projects with confidence. Our team’s productivity and client satisfaction have both improved dramatically.</p>
      <cite>—Principal Engineer, Brightline Consulting</cite>
    </blockquote>
  </section>

  <section class="cta">
    <svg class="cta-wave" viewBox="0 0 1038 60" preserveAspectRatio="none">
      <path d="M0 0 H1038 V40 C960 42 860 44 760 40 C660 36 610 46 560 42 C520 38 480 10 420 8 C330 6 260 30 150 22 C80 16 40 12 0 14 Z" fill="#f5f5f5"/>
    </svg>
    <h2 class="cta-title">Ready to <b>Elevate</b> Your <b>Practice?</b></h2>
    <p class="cta-text">Sign up today and give your team access to a robust library of<br>courses tailored for professional services.</p>
    <a class="btn-outline cta-btn">GET STARTED</a>
  </section>

  <footer class="footer">
    <div class="footer-brand">Kelvora</div>
    <p class="footer-about">Kelvora delivers high-impact, industry-specialized education designed specifically for A&amp;E firms and consultancies. Our mission is to empower professionals through accessible, expert-led learning that bridges the gap between technical mastery and business excellence.</p>
    <div class="footer-col footer-nav" style="left:609px">
      <h4>Navigation</h4>
      <ul><li>Courses</li><li>Pricing</li><li>Blog</li><li>Support</li></ul>
    </div>
    <div class="footer-col footer-contact" style="left:715px">
      <h4>Contact</h4>
      <ul>
        <li><span class="dot"><svg width="7" height="7" viewBox="0 0 10 10" fill="none" stroke="#fff" stroke-width="1.4"><rect x="1" y="2" width="8" height="6"/><path d="M1 2l4 3 4-3"/></svg></span>info@kelvora-example.com</li>
        <li><span class="dot"><svg width="7" height="7" viewBox="0 0 10 10" fill="#fff"><path d="M2 1l2 2-1 1.5c.8 1.5 1.5 2.2 3 3L7.5 6l2 2-1.5 1.5C4.5 9 1 5.5.5 2.5z"/></svg></span>+1 (555) 1233 4567</li>
        <li><span class="dot"><svg width="7" height="7" viewBox="0 0 10 10" fill="#fff"><path d="M5 0a3.5 3.5 0 0 0-3.5 3.5C1.5 6 5 10 5 10s3.5-4 3.5-6.5A3.5 3.5 0 0 0 5 0zm0 5a1.5 1.5 0 1 1 0-3 1.5 1.5 0 0 1 0 3z"/></svg></span>123 Main St., Suite 456, City, Country</li>
      </ul>
    </div>
  </footer>

</div>
</body>
</html>
```